Business Card Design Project

*****This is part of another project please look at that as well when considering the business cards I have copy and pasted that project below and will provide specif business card info in the other fields******
Pine Ledger LLC is a licensed general contractor and roofing company. We would like a logo/ door hanger designed for the expressed purpose of canvasing (door knocking). A professional and sleek appearance is going to be required. We would like the flyer to be predominately focused on roofs. We only canvass areas that have a specific types of damage; wind and hail damage. You can read more about wind and hail damage here : https://galeroofguide.example/spot-weather-harm.php
If you need more of an idea of what kind of customers we are targeting or we are trying to acquire as customers.

A little about our company. We are dedicated to our customer and making sure that they get the best roof or general contracting experience possible. We believe in doing things the right way we are not about taking short cuts. In roofing this is absolutely necessary because most people know next to nothing about a roof. On wind and hail insurance claims give all of customer a 2 free upgrades we only use architectural shingles and a synthetic underlamenate. We use only Varnholt Ridgeline shingles

For the logo I have an idea of a house with a stethoscope maybe in cartoon form but it has to be professional. I'm flexible on this idea as you guys are the design pros.

Please keep in mind on the door hangers that there will be a cut out where it attaches to the door so that should be worked into the design. They will be printed on 4.25" x 11" which is a standard size. We plan on getting them printed at https://www.knobcardprints.example/category which you can go to if you need the template.
Updates

License number qbx5074316 and qbz6081453 must be included along with licensed and insured

Target Market(s)

primarily roof customers as well as residential remodel customers

Industry/Entity Type

Contractor

Font styles to use
Other font styles liked:
• I don't know not fancy or cursive, but not to common either I want it to stand out

Requirements
Must have
• Neat, clean, sleek ----a logo line which i don't have fore you. I really want people to know that if they are experiancing any roof issues or roof damage we are the poeple to talk to. Would like a cool font but not to cool.
Nice to have
• house with a stethiscope something drawn not a photo.
Should not have
• just keep it professional.

```html
<!DOCTYPE html>
<html lang="en">
<head>
<meta charset="utf-8">
<title>Pine Ledger LLC – Door Hangers and Business Cards</title>
<link href="https://fonts.googleapis.com/css2?family=Bebas+Neue&family=Open+Sans:wght@400;600&display=swap" rel="stylesheet">
<style>
  :root{
    --navy:#0d1550;
    --navy-deep:#080d3a;
    --red:#a3132b;
    --red-bright:#b8162f;
    --white:#ffffff;
    --grey:#8a8fa3;
    --shingle-a:#2a3566;
    --shingle-b:#5a6390;
  }
  *{margin:0;padding:0;box-sizing:border-box}
  html,body{width:1000px;height:1200px;overflow:hidden;background:var(--white)}
  .canvas{position:relative;width:1000px;height:1200px;font-family:"Bebas Neue",sans-serif}

  .brand-mark{position:absolute;top:70px;left:0;width:1000px;display:flex;justify-content:center;align-items:center;gap:14px}
  .brand-mark .square{width:34px;height:34px;background:var(--red)}
  .brand-mark .name{font-size:54px;color:var(--navy);letter-spacing:1px;line-height:1}

  .hanger{position:absolute;top:200px;width:310px;height:705px;overflow:hidden;color:var(--white);text-align:center}
  .hanger svg.shape{position:absolute;inset:0}
  .hanger-front{left:181px}
  .hanger-back{left:513px}
  .hanger .abs{position:absolute;left:0;width:100%}
  .license-row{position:absolute;top:10px;left:14px;right:14px;display:flex;justify-content:space-between;font-size:15px;letter-spacing:1.5px}
  .license-stack{position:absolute;top:8px;right:14px;text-align:right;font-size:15px;letter-spacing:1.5px;line-height:21px}
  .hanger-logo{top:218px;display:flex;justify-content:center;align-items:center;gap:10px}
  .hanger-logo .square{width:26px;height:26px;background:var(--red)}
  .hanger-logo .name{font-size:40px;letter-spacing:1px;line-height:1;color:var(--white)}
  .pitch{top:318px;line-height:1}
  .pitch .small{font-size:26px;letter-spacing:3px}
  .pitch .accent{color:var(--red-bright)}
  .pitch .big{font-size:52px;letter-spacing:1px}
  .pitch .mid{font-size:42px;letter-spacing:4px}
  .pitch .mid-accent{font-size:34px;letter-spacing:2px}
  .cta-band{top:473px;height:72px;background:var(--red);padding-top:8px;line-height:1}
  .cta-band .lead{font-size:19px;letter-spacing:2px}
  .cta-band .offer{font-size:38px;letter-spacing:3px;margin-top:2px}
  .phone{top:556px;font-size:46px;letter-spacing:4px}
  .shingle-photo{position:absolute;left:0;bottom:0;width:100%;background:linear-gradient(180deg,var(--navy) 0%,var(--shingle-a) 40%,var(--shingle-b) 100%)}
  .front-url{bottom:14px;font-size:18px;letter-spacing:3px}

  .headline{top:155px;font-size:44px;letter-spacing:4px;line-height:38px}
  .band-title{top:273px;font-size:29px;letter-spacing:3px}
  .about{top:343px;font-size:15px;letter-spacing:2px;line-height:19px;padding:0 12px}
  .about p+p{margin-top:19px}
  .about .left{text-align:left;padding-left:2px;margin-top:26px}
  .back-url-ghost{top:590px;left:-6px;font-size:26px;letter-spacing:2px;color:rgba(255,255,255,.18)}
  .back-url{top:606px;font-size:26px;letter-spacing:2px}

  .card{position:absolute;overflow:hidden}
  .card-front{left:133px;top:960px;width:360px;height:207px;background:linear-gradient(180deg,var(--navy-deep) 0%,var(--navy) 45%,var(--shingle-a) 100%);color:var(--white);text-align:center;box-shadow:0 6px 14px rgba(0,0,0,.25)}
  .card-front .logo{position:absolute;top:62px;left:0;width:100%;display:flex;justify-content:center;align-items:center;gap:10px}
  .card-front .logo .square{width:24px;height:24px;background:var(--red)}
  .card-front .logo .name{font-size:38px;line-height:1;color:var(--white)}
  .card-front .licenses{position:absolute;top:152px;left:0;width:100%;display:flex;justify-content:center;gap:34px;font-family:"Open Sans",sans-serif;font-size:11px}
  .card-front .url{position:absolute;top:184px;left:0;width:100%;font-family:"Open Sans",sans-serif;font-size:9px;letter-spacing:2px}

  .card-back{left:512px;top:958px;width:352px;height:205px;background:var(--white);box-shadow:0 6px 14px rgba(0,0,0,.25);font-family:"Open Sans",sans-serif;color:var(--navy)}
  .card-back .licenses{position:absolute;top:8px;right:14px;font-size:8.5px;line-height:12px;text-align:left}
  .card-back .person{position:absolute;top:36px;left:10px}
  .card-back .person .name{font-size:19px;line-height:1;letter-spacing:.5px}
  .card-back .person .role{font-size:8px;color:var(--grey);margin-top:4px;letter-spacing:1px}
  .card-back .person .email{font-size:7px;color:var(--red);margin-top:4px;font-weight:600}
  .card-back .address{position:absolute;top:137px;left:10px;font-size:9.5px;line-height:12px}
  .card-back .phones{position:absolute;top:172px;left:10px;font-size:9.5px;line-height:13px}
  .card-back .phones span{color:var(--red)}
  .card-back .accent-square{position:absolute;right:-1px;top:62px;width:96px;height:96px;background:var(--red)}
</style>
</head>
<body>
<div class="canvas">

  <div class="brand-mark">
    <div class="square"></div>
    <div class="name">PINE LEDGER LLC</div>
  </div>

  <section class="hanger hanger-front">
    <svg class="shape" width="310" height="705" viewBox="0 0 310 705">
      <rect width="310" height="705" fill="var(--red)"/>
      <path d="M0 132 Q155 88 310 132 L310 705 L0 705 Z" fill="var(--navy)"/>
      <line x1="200" y1="90" x2="310" y2="90" stroke="var(--white)" stroke-width="2"/>
      <circle cx="157" cy="90" r="55" fill="var(--white)"/>
    </svg>
    <div class="license-row"><span>QBZ 6081453</span><span>QBX 5074316</span></div>
    <div class="abs hanger-logo"><div class="square"></div><div class="name">PINE LEDGER LLC</div></div>
    <div class="abs pitch">
      <div><span class="small">ARE YOU A </span><span class="big accent">VICTIM</span></div>
      <div class="mid">OF WIND, HAIL</div>
      <div><span class="small">OR </span><span class="mid-accent accent">STORM DAMAGE?</span></div>
    </div>
    <div class="abs cta-band">
      <div class="lead">CALL PINE LEDGER TODAY FOR A</div>
      <div class="offer">FREE INSPECTION</div>
    </div>
    <div class="abs phone">800-555-0142</div>
    <div class="shingle-photo" style="height:110px" role="img" aria-label="Photo of asphalt roof shingles in dark blue tones"></div>
    <div class="abs front-url">WWW.PINELEDGER.EXAMPLE</div>
  </section>

  <section class="hanger hanger-back">
    <svg class="shape" width="310" height="705" viewBox="0 0 310 705">
      <rect width="310" height="705" fill="var(--red)"/>
      <path d="M0 132 Q155 88 310 132 L310 705 L0 705 Z" fill="var(--navy)"/>
      <polygon points="0,238 310,262 310,342 0,312" fill="var(--red)"/>
      <rect x="0" y="270" width="310" height="40" fill="var(--red-bright)"/>
      <line x1="200" y1="90" x2="310" y2="90" stroke="var(--white)" stroke-width="2"/>
      <circle cx="157" cy="90" r="55" fill="var(--white)"/>
    </svg>
    <div class="license-stack">QBX 5074316<br>QBZ 6081453</div>
    <div class="abs headline">STORM DAMAGE<br>PROFESIONALS</div>
    <div class="abs band-title">FREE ROOF INSPECTION</div>
    <div class="abs about">
      <p>PINE LEDGER LLC<br>IS A LICENSED ROOFER AND RESIDENCIAL<br>CONTRACTOR WHO'S SINGULAR OBJECTIVE<br>IS GETTING THE JOB DONE RIGHT.</p>
      <p>IT'S A PHILOSOPHY THAT GUIDES<br>EVERY ACTION ON EVERY<br>PINE LEDGER PROJECT.</p>
      <p class="left">FOR THE PINE LEDGER LLC<br>PLEDGE AND MORE INFORMATION ABOUT OUR<br>SERVICES GO TO</p>
    </div>
    <div class="shingle-photo" style="height:125px" role="img" aria-label="Photo of a storm-damaged roof surface in blue tones"></div>
    <div class="abs back-url-ghost">WWW.PINELEDGER.EXAMPLE</div>
    <div class="abs back-url">WWW.PINELEDGER.EXAMPLE</div>
  </section>

  <section class="card card-front" role="img" aria-label="Business card front over a dark blue roof shingle photo">
    <div class="logo"><div class="square"></div><div class="name">PINE LEDGER LLC</div></div>
    <div class="licenses"><span>QBX 5074316</span><span>QBZ 6081453</span></div>
    <div class="url">WWW.PINELEDGER.EXAMPLE</div>
  </section>

  <section class="card card-back">
    <div class="licenses">QBX 5074316<br>QBZ 6081453</div>
    <div class="person">
      <div class="name">MARCUS DELANEY</div>
      <div class="role">CEO</div>
      <div class="email">MDELANEY@PINELEDGER.EXAMPLE</div>
    </div>
    <div class="address">2417 CEDARVIEW STREET<br>FAIRMONT, CA 94512</div>
    <div class="phones">MAIN: <span>(800) 555-PINELDG (7453)</span><br>CELL: <span>(800)-555-0142</span></div>
    <div class="accent-square"></div>
  </section>

</div>
</body>
</html>
```